Custom T Shirt Site Needs New Graphics for Homepage.

I am looking to have the homepage graphic redone. They need to unique images and give the site a fresh look. www.quillbarnet.com. I want new banners, New images for T Shirts, Polo Shirts, Sweatshirts, Hats, Jersey. I want the large banner on the homepage changed and the 3 banners to the right and below. I would look at a new layout of the homepage.

Reason: Some are still sending desings

```html
<!DOCTYPE html>
<html lang="en">
<head>
<meta charset="utf-8">
<title>Quillbarnet – Custom T-Shirts</title>
<link rel="stylesheet" href="https://fonts.googleapis.com/css2?family=Source+Sans+3:wght@400;600&family=Arimo:wght@400;700&family=Lora:ital@1&display=swap">
<style>
:root{
  --page:#ffffff;
  --top-bg:#f4f4f4;
  --stripe:#e6e6e6;
  --navy:#1a4a82;
  --navy-dark:#16457a;
  --heading:#1f4f8a;
  --text:#333333;
  --muted:#6a5a4a;
  --green:#3b9a3b;
  --rule:#dcdcdc;
  --gold:#d8c9a8;
  --orange:#f08a1c;
  --banner-blue:#5d9fd6;
  --banner-blue-dark:#3f7fbf;
}
*{margin:0;padding:0;box-sizing:border-box}
html,body{width:1052px;height:1200px;overflow:hidden;background:var(--page)}
body{position:relative;font-family:"Arimo",Arial,sans-serif;color:var(--text)}
.abs{position:absolute}
.top-area{left:0;top:0;width:1052px;height:312px;background:var(--top-bg)}
.stripe{left:0;width:1052px;height:10px;background:repeating-linear-gradient(90deg,var(--stripe) 0 2px,#f2f2f2 2px 4px)}
.hero{left:140px;top:0;width:772px;height:232px;background:linear-gradient(135deg,var(--banner-blue),var(--banner-blue-dark));border:1px solid #c9d08a}
.tabs{left:140px;top:232px;width:774px;height:52px;display:flex;background:#fff;box-shadow:0 3px 5px rgba(0,0,0,.25)}
.tab{flex:1;display:flex;align-items:center;gap:6px;padding-left:6px;border-right:1px solid #ddd}
.tab:last-child{border-right:none}
.tab-thumb{width:34px;height:34px;border:1px solid #ccc;background:#eee}
.tab-title{font-family:"Source Sans 3",sans-serif;font-size:14px;color:var(--navy)}
.tab-sub{font-size:8px;color:#444}
.section-title{font-family:"Source Sans 3",sans-serif;font-size:24px;color:var(--heading)}
.rule{height:1px;background:var(--rule)}
.shirt{width:170px;height:170px}
.price{width:180px;text-align:center;font-weight:700;font-size:14px;color:#444;line-height:18px}
.price b{color:var(--green)}
.side-box{width:194px;background:#fff;box-shadow:0 1px 3px rgba(0,0,0,.25)}
.side-head{background:var(--navy);color:#fff;font-family:"Source Sans 3",sans-serif;font-size:17px;height:27px;line-height:27px;padding-left:12px;display:flex;align-items:center;gap:8px}
.side-item{padding:5px 12px 4px;border-bottom:1px solid var(--gold)}
.side-item:last-child{border-bottom:none}
.side-item h4{font-size:11px;color:var(--navy);letter-spacing:.5px;font-weight:700}
.side-item p,.side-note{font-family:"Lora",serif;font-style:italic;font-size:8.5px;color:var(--muted);line-height:12px}
.check-list{list-style:none;padding:8px 16px 4px}
.check-list li{font-size:11px;font-weight:700;color:var(--navy);line-height:19px;display:flex;align-items:center;gap:7px}
.link-col{list-style:none;font-size:11.5px;line-height:23.3px;color:#333}
.btn{background:var(--navy-dark);color:#fff;border-radius:4px;font-size:13px;text-align:center;line-height:23px}
.cats{font-size:13px;line-height:23.3px;list-style:none}
.text-link{font-size:11px;color:var(--navy);text-decoration:underline}
.about{font-size:11.3px;line-height:19px;color:#333}
</style>
</head>
<body>
<div class="abs top-area"></div>
<div class="abs hero" role="img" aria-label="Hero banner: a hand-drawn sum of you plus a black printed t-shirt equals a happy stick figure wearing it, on blue grunge texture"></div>
<nav class="abs tabs">
  <div class="tab"><div class="tab-thumb" role="img" aria-label="Grey t-shirt thumbnail"></div><div><div class="tab-title">T-Shirts</div><div class="tab-sub">Click here to see more</div></div></div>
  <div class="tab"><div class="tab-thumb" role="img" aria-label="Orange polo shirt thumbnail" style="background:#f4a070"></div><div><div class="tab-title">Polo Shirts</div><div class="tab-sub">Click here to see more</div></div></div>
  <div class="tab"><div class="tab-thumb" role="img" aria-label="Blue sweatshirt thumbnail" style="background:#9db0cf"></div><div><div class="tab-title">Sweatshirts</div><div class="tab-sub">Click here to see more</div></div></div>
  <div class="tab"><div class="tab-thumb" role="img" aria-label="Yellow cap thumbnail" style="background:#f3cc55"></div><div><div class="tab-title">Hats &amp; Caps</div><div class="tab-sub">Click here to see more</div></div></div>
  <div class="tab"><div class="tab-thumb" role="img" aria-label="Navy and white jersey thumbnail" style="background:#c7cbe0"></div><div><div class="tab-title">Jerseys</div><div class="tab-sub">Click here to see more</div></div></div>
</nav>
<div class="abs stripe" style="top:310px"></div>

<svg class="abs" style="left:148px;top:348px" width="34" height="34" viewBox="0 0 34 34"><circle cx="17" cy="17" r="16" fill="var(--orange)" stroke="#f7c27a" stroke-width="2"/><path d="M11 12l4-2h4l4 2 2 4-3 1v7h-10v-7l-3-1z" fill="#fff"/></svg>
<h2 class="abs section-title" style="left:190px;top:346px">T-Shirts Styles</h2>
<div class="abs rule" style="left:148px;top:390px;width:758px"></div>

<div class="abs shirt" role="img" aria-label="Orange t-shirt" style="left:156px;top:408px;background:#f08a48"></div>
<div class="abs shirt" role="img" aria-label="Blue t-shirt" style="left:338px;top:408px;background:#6d8fc8"></div>
<div class="abs shirt" role="img" aria-label="Green t-shirt" style="left:522px;top:408px;background:#1f8a4a"></div>
<div class="abs price" style="left:146px;top:585px">Price: <b>US $65</b><br>COD: AE001</div>
<div class="abs price" style="left:328px;top:585px">Price: <b>US $65</b><br>COD: AE001</div>
<div class="abs price" style="left:510px;top:585px">Price: <b>US $65</b><br>COD: AE001</div>

<aside class="abs side-box" style="left:713px;top:401px;height:229px">
  <div class="side-head">Our Products</div>
  <div class="side-item"><h4>FREEE SHIPPING</h4><p>Order T-shirts Today...</p></div>
  <div class="side-item"><h4>FREE 2-WEEK DELIVERY</h4><p>Guaranteed by Fri, Mar 21</p></div>
  <div class="side-item"><h4>RUSH 1-WEEK DELIVERY</h4><p>Guaranteed by Sat, Mar 15</p></div>
  <div class="side-item"><h4>NEED IT SOONER?</h4><p>Ask about Super Rush Delivery<br>View Daily Delivery Calendar</p></div>
</aside>

<h2 class="abs section-title" style="left:176px;top:696px">You Create</h2>
<ul class="abs link-col" style="left:180px;top:736px"><li>T Shirt</li><li>Cheap T-Shirts</li><li>Baby Clothing</li><li>Corporate Logo Apparel</li><li>Vinyl Banners</li><li>Cistom Unifoems</li></ul>
<ul class="abs link-col" style="left:360px;top:736px"><li>Sweatshirts</li><li>Womens Apparel</li><li>Hats</li><li>Family Reunions T-Shirts</li><li>Personalized Wedding Gifts</li><li>Jerseys</li></ul>
<ul class="abs link-col" style="left:562px;top:736px"><li>Polo Shirts</li><li>Teen Apparel</li><li>Bags</li><li>Custom Golf Apparel</li><li>Posters</li></ul>
<div class="abs btn" style="left:559px;top:883px;width:119px;height:23px">See All Products</div>

<aside class="abs side-box" style="left:713px;top:704px;height:148px">
  <div class="side-head"><svg width="16" height="18" viewBox="0 0 16 18"><path d="M8 1l6 2v6c0 4-3 7-6 8-3-1-6-4-6-8V3z" fill="none" stroke="#fff" stroke-width="1.6"/><text x="8" y="13" font-size="9" fill="#fff" text-anchor="middle" font-family="Arimo">$</text></svg>All-inclusive Pricing</div>
  <ul class="check-list">
    <li><svg width="9" height="9"><path d="M4.5 0l4.5 4.5-4.5 4.5L0 4.5z" fill="var(--navy)"/></svg>No hidden fees</li>
    <li><svg width="9" height="9"><path d="M4.5 0l4.5 4.5-4.5 4.5L0 4.5z" fill="var(--navy)"/></svg>No setup charges</li>
    <li><svg width="9" height="9"><path d="M4.5 0l4.5 4.5-4.5 4.5L0 4.5z" fill="var(--navy)"/></svg>Free artist review</li>
  </ul>
  <div class="rule" style="margin:4px 12px;background:var(--gold)"></div>
  <p class="side-note" style="padding:2px 12px">Learn How Pricing Works</p>
</aside>

<h2 class="abs section-title" style="left:176px;top:954px">Designs Ideas Categories</h2>
<div class="abs rule" style="left:148px;top:992px;width:750px"></div>
<ul class="abs cats" style="left:187px;top:1009px"><li>Sports (0)</li><li>Events (0)</li><li>Business (0)</li><li>Holiday (0)</li></ul>
<ul class="abs cats" style="left:373px;top:1009px"><li>School (0)</li><li>Religious (0)</li><li>Military (0)</li></ul>
<span class="abs text-link" style="left:309px;top:1095px">Most Popular Templates</span>
<div class="abs" style="left:485px;top:1002px;width:1px;height:146px;background:var(--navy)"></div>
<p class="abs about" style="left:533px;top:1010px;width:364px">If you're running out of ideas about the style, design, layout and colors for your custom shirts, Quillbarnet has over 250 Design Ideas that you can use as a guide for your t-shirt creation. These design ideas were created by our very own team of in-house artists. You can modify the color, the style and the text on the shirt according to your preferences. You can start by browsing the design ideas categories on the left.</p>
<span class="abs" style="left:533px;top:1142px;font-size:10.5px;color:var(--navy);font-weight:700">Read More...</span>
<div class="abs stripe" style="top:1188px;height:12px"></div>
</body>
</html>
```